Kellow Family Law, legal technician needs a website and design

I need a website for a family law practice. I specialize in collaborative law, unbundled services, and mediation. The website must contain my company logo (file attached), and the website must be a mixture of my personality and my profession. I have attached additional information to explain my personality and profession.

Target Market(s)

Lower through middle-class (income level up to $200,000 per year)

Coding

Coded - Design and coding required

Number of Pages Required

1 page

Requirements
Must have
• Must have enough pages to cover required content. I submitted below some content about the collaborative law process. All of the content is not necessary. However, the website must have enough content to clearly describe the services I offer. Use your professionalism and judgment regarding font, font size, etc.

```html
<!DOCTYPE html>
<html lang="en">
<head>
<meta charset="utf-8">
<title>Kellow Family Law</title>
<link rel="stylesheet" href="https://fonts.googleapis.com/css2?family=Josefin+Sans:wght@400;600;700&family=Montserrat:wght@400;500;600;700&display=swap">
<style>
:root{
  --navy:#0d1b52;
  --navy-deep:#081238;
  --olive:#c3c24a;
  --ink:#1c1c1c;
  --muted:#666;
  --card:#fafafa;
  --footer:#0f0f10;
  --white:#fff;
}
*{box-sizing:border-box;margin:0;padding:0}
html,body{width:1200px;height:4431px;overflow:hidden}
body{position:relative;font-family:'Montserrat',sans-serif;color:var(--ink);background:var(--white)}
.abs{position:absolute}
.heading{font-family:'Josefin Sans',sans-serif;font-weight:700;letter-spacing:.5px}
.eyebrow{font-family:'Montserrat',sans-serif;color:var(--olive);font-size:18px}
.btn{position:absolute;display:flex;align-items:center;justify-content:center;background:var(--olive);color:var(--ink);font-family:'Josefin Sans',sans-serif;font-weight:700;font-size:15px;border-radius:3px}
.centered{left:0;width:1200px;text-align:center}

/* top bar + hero */
.hero{position:absolute;left:0;top:0;width:1200px;height:595px;background:linear-gradient(100deg,#1c2244 0%,#3a3a55 40%,#7a6a60 70%,#2b3560 100%)}
.hero-shade{position:absolute;inset:0;background:linear-gradient(90deg,rgba(10,18,50,.75),rgba(10,18,50,.15))}
.topbar{position:absolute;left:0;top:0;width:1200px;height:31px;background:var(--navy-deep);color:#fff;font-size:11px}
.topbar span{position:absolute;top:9px}
.logo{position:absolute;display:flex;align-items:center;gap:10px;color:var(--olive);font-family:'Josefin Sans',sans-serif;font-weight:700}
.logo i{display:block;width:34px;height:34px;border:2px solid var(--olive)}
.nav a{position:absolute;top:58px;color:#fff;font-size:12px;text-decoration:none}
.hero h1{position:absolute;left:186px;color:#fff}
.hero p{position:absolute;left:186px;top:322px;width:420px;color:#fff;font-size:15px;line-height:23px}
.ghost{background:transparent;border:2px solid #fff;color:#fff}
.chat{position:absolute;left:1044px;top:480px;width:94px;height:45px;border-radius:23px;background:var(--olive);display:flex;align-items:center;gap:10px;padding-left:8px;color:#fff;font-size:15px}
.chat i{display:block;width:28px;height:28px;border-radius:50%;background:#fff}

/* who */
.photo{position:absolute}
.who p{position:absolute;left:627px;top:828px;width:375px;font-size:14.5px;line-height:22.4px;color:#444}

/* cards */
.svc{position:absolute;top:1403px;width:262px}
.svc .pic{height:177px}
.svc h3{font-family:'Josefin Sans',sans-serif;font-weight:700;font-size:14.5px;line-height:22px;margin:22px 4px 0;color:var(--ink)}
.svc p{font-size:11.5px;line-height:18px;color:#555;margin:10px 4px 0}
.svc .meta{position:absolute;top:320px;left:4px;right:4px;display:flex;justify-content:space-between;font-size:12px;color:var(--olive)}
.svc .meta b{font-weight:700}
.svc .meta small{color:#555;font-size:10px}

/* video */
.video{position:absolute;left:0;top:1833px;width:1200px;height:488px;background:var(--navy)}
.video .clip{position:absolute;border:3px solid #fff;border-radius:4px}
.play{position:absolute;left:50%;top:50%;width:26px;height:26px;margin:-13px;border-radius:50%;background:rgba(255,255,255,.8)}

/* testimonials */
.quote{position:absolute;top:2501px;width:406px;height:241px;background:#fff;box-shadow:0 4px 18px rgba(0,0,0,.07);border-radius:4px}
.quote .av{position:absolute;left:30px;top:26px;width:44px;height:44px;border-radius:50%;background:#e9d9d3}
.quote .nm{position:absolute;left:96px;top:30px;font-family:'Josefin Sans',sans-serif;font-weight:700;font-size:17px}
.quote .rl{position:absolute;left:96px;top:55px;font-size:11px;color:#888}
.quote .st{position:absolute;right:30px;top:34px;color:var(--olive);font-size:13px;letter-spacing:2px}
.quote p{position:absolute;left:30px;top:100px;width:340px;font-size:13.5px;line-height:22px;color:#555}
.arrow{position:absolute;width:34px;height:34px;border-radius:50%;display:flex;align-items:center;justify-content:center;font-size:15px}
.arrow.light{background:#fff;box-shadow:0 2px 10px rgba(0,0,0,.1);color:#333}
.arrow.olive{background:var(--olive);color:#fff}
.dot{position:absolute;top:2804px;width:6px;height:6px;border-radius:50%;background:#bbb}

/* help */
.help{position:absolute;left:0;top:2904px;width:1200px;height:318px;background:var(--navy)}

/* blogs */
.post{position:absolute;top:3409px;width:262px;height:399px;background:var(--card)}
.post .pic{height:206px}
.post h3{font-family:'Montserrat',sans-serif;font-weight:600;font-size:14.5px;line-height:20px;margin:26px 26px 0}
.post p{font-size:11.5px;line-height:19px;color:#666;margin:14px 26px 0}
.post .more{position:absolute;left:26px;top:352px;color:var(--olive);font-weight:700;font-size:13px}

/* footer */
.footer{position:absolute;left:0;top:3890px;width:1200px;height:541px;background:var(--footer);color:#fff}
.footer h4{position:absolute;top:251px;font-family:'Montserrat',sans-serif;font-weight:600;font-size:14px}
.footer ul{position:absolute;top:296px;list-style:none;font-size:11.5px;line-height:30px}
.footer .about{position:absolute;left:186px;top:298px;width:230px;font-size:11.5px;line-height:19px}
.contact-row{position:absolute;left:803px;display:flex;gap:18px;font-size:11.5px;line-height:19px;width:220px}
.contact-row svg{flex:none;margin-top:2px}
</style>
</head>
<body>

<section class="hero">
  <div role="img" aria-label="Photo of a determined woman in a navy blazer" style="position:absolute;inset:0;background:radial-gradient(ellipse at 70% 40%,#9a8a80 0%,#4c4a60 45%,#1b2246 100%)"></div>
  <div class="hero-shade"></div>
  <div class="topbar">
    <span style="left:186px">☎&nbsp;&nbsp; +(00) 0555 210 478</span>
    <span style="left:346px">✉&nbsp;&nbsp; hello@kellowlaw.com</span>
    <span style="left:809px">Follow us on:&nbsp;&nbsp; ● ● ● ●</span>
    <span style="left:989px">EN ▾</span>
  </div>
  <div class="logo" style="left:186px;top:48px"><i></i><span style="font-size:15px;line-height:16px">KELLOW<br><span style="font-size:10px;font-weight:600">FAMILY LAW</span></span></div>
  <nav class="nav">
    <a style="left:512px">Home</a><a style="left:578px">Our Service</a><a style="left:676px">News</a><a style="left:738px">Videos</a><a style="left:808px;color:var(--olive)">Contact</a>
  </nav>
  <div class="btn" style="left:889px;top:46px;width:125px;height:42px;font-size:11px">Get Consultation</div>
  <h1 class="heading" style="top:186px;font-size:44px;font-weight:400">Need any help?</h1>
  <h1 class="heading" style="top:242px;font-size:54px">We Fight For Right</h1>
  <p>Kellow Family Law, collaborative law and unbundled legal services in King County, Washington state</p>
  <div class="btn" style="left:186px;top:404px;width:130px;height:45px">Contact Us</div>
  <div class="btn ghost" style="left:340px;top:404px;width:133px;height:45px">Our Service</div>
  <div class="chat"><i></i>Chat</div>
</section>

<section class="who">
  <div class="photo" style="left:162px;top:973px;width:209px;height:251px;background:var(--olive)"></div>
  <div class="photo" role="img" aria-label="Portrait of a lawyer in a dark suit with arms crossed" style="left:186px;top:672px;width:405px;height:528px;background:linear-gradient(160deg,#4a3f38,#1e1a18)"></div>
  <div class="abs eyebrow" style="left:627px;top:686px">Who We Are</div>
  <h2 class="abs heading" style="left:627px;top:730px;font-size:29px;line-height:38px">We Always Fight For Your<br>Justice To Win</h2>
  <p>Lorem ipsum dolor sit amet, consectetur adipisicing elit, sed do eiusmod tempor incididunt ut labore et dolore magna aliqua. Ut enim ad minim veniam, quis nostrud exercitation ullamco laboris nisi ut aliquip ex ea commodo consequat. Duis aute irure dolor in reprehenderit in voluptate velit esse cillum dolore eu fugiat nulla pariatur. Excepteur sint occaecat cupidatat non proident, sunt in culpa qui officia deserunt.</p>
  <div class="btn" style="left:627px;top:1064px;width:152px;height:57px">Learn More</div>
</section>

<section class="services">
  <div class="abs eyebrow centered" style="top:1300px">Our Service</div>
  <h2 class="abs heading centered" style="top:1336px;font-size:30px">How Its Work</h2>
  <article class="svc" style="left:184px">
    <div class="pic" role="img" aria-label="Couple meeting with a mediator at a table" style="background:linear-gradient(135deg,#d8d2cc,#8a8078)"></div>
    <h3>Settlement Agreement, Child Support, and Divorce Paperwork</h3>
    <p>You've talked and you both agree on exactly what you want to do your assets, your child support.</p>
    <div class="meta"><span>Read More&nbsp; ⟶</span><span><b>$1,499</b><small>/court fee</small></span></div>
  </article>
  <article class="svc" style="left:469px">
    <div class="pic" role="img" aria-label="Child holding a teddy bear while parents argue" style="background:linear-gradient(135deg,#c9c2b8,#7d7266)"></div>
    <h3>Comprehensive Settlement Agreem -ent and Divorce Paperwork</h3>
    <p>You need neutral advice to settle on an asset/debt division, buyout for real pro perty, or other issues.</p>
    <div class="meta"><span>Read More&nbsp; ⟶</span><span><b>1,898</b><small>/court fee</small></span></div>
  </article>
  <article class="svc" style="left:755px">
    <div class="pic" role="img" aria-label="Person raising arms at a seaside sunset" style="background:linear-gradient(180deg,#3d5a8a 0%,#c9a27a 60%,#3a3430 100%)"></div>
    <h3>Mediation</h3>
    <p>Mediation to help you reach an agreement dolor sit amet, consectetur adipisicing elit, sed do eiusmod tempor incididunt.</p>
    <div class="meta"><span>Read More&nbsp; ⟶</span><span><b>$250</b><small>/ per hour</small></span></div>
  </article>
</section>

<section class="video">
  <div class="abs" style="left:184px;top:103px;color:#fff;font-size:17px">Explore our video</div>
  <h2 class="abs heading" style="left:186px;top:150px;color:#fff;font-size:31px;line-height:38px">We Help Resolve Life's<br>Challenge</h2>
  <p class="abs" style="left:186px;top:240px;width:320px;color:#fff;font-size:15px;line-height:22.5px">Lorem ipsum dolor sit amet consectetur adipisicing elit sed do eiusmod tempor incidid unt ut labore et.</p>
  <div class="btn" style="left:186px;top:328px;width:135px;height:51px;font-size:13px">Watch Now!</div>
  <div class="clip" role="img" aria-label="Video still of a parent embracing a child" style="left:564px;top:75px;width:210px;height:337px;background:linear-gradient(160deg,#5a4e44,#1d1a18)"><span class="play"></span></div>
  <div class="clip" role="img" aria-label="Video still of a courtroom assembly" style="left:793px;top:75px;width:223px;height:120px;background:linear-gradient(160deg,#4f6a5c,#1e2c28)"><span class="play"></span></div>
  <div class="clip" role="img" aria-label="Video still of a lawyer presenting to an audience" style="left:793px;top:211px;width:223px;height:201px;background:linear-gradient(160deg,#a0876a,#3b2f26)"><span class="play"></span></div>
</section>

<section class="testimonials">
  <div class="abs eyebrow centered" style="top:2393px">Testimonial</div>
  <h2 class="abs heading centered" style="top:2434px;font-size:30px">What Our Clients Say</h2>
  <div class="arrow light" style="left:110px;top:2594px">‹</div>
  <div class="arrow olive" style="left:1058px;top:2594px">›</div>
  <div class="quote" style="left:186px">
    <div class="av" role="img" aria-label="Client avatar"></div>
    <div class="nm">Marissa T</div><div class="rl">a Divorce client</div><div class="st">★★★★★</div>
    <p>Attorney Kellow represented me in both divorce and bankruptcy proceedings. Never once did I doubt I was in the best possible hands. Phone calls were returned without delay. I'd recommend Attorney Kellow.</p>
  </div>
  <div class="quote" style="left:612px">
    <div class="av" role="img" aria-label="Client avatar"></div>
    <div class="nm">Dana L</div><div class="rl">a Divorce client</div><div class="st">★★★★★</div>
    <p>My ex-fiance and I bought a car together 5 years ago. We broke up a few months after the purchase and ever since then I have been asking him to take me off of the loan. He of course refused Thanks.</p>
  </div>
  <span class="dot" style="left:566px;background:var(--olive)"></span><span class="dot" style="left:595px"></span><span class="dot" style="left:616px"></span><span class="dot" style="left:637px"></span>
</section>

<section class="help">
  <svg class="abs" style="left:0;top:0" width="580" height="318" viewBox="0 0 580 318" role="img" aria-label="Photo of lawyers consulting with clients in an office">
    <defs><linearGradient id="helpPhoto" x1="0" y1="0" x2="1" y2="1"><stop offset="0" stop-color="#8a7a6c"/><stop offset="1" stop-color="#2c2a2e"/></linearGradient></defs>
    <polygon points="0,0 473,0 567,318 0,318" fill="url(#helpPhoto)"/>
    <line x1="473" y1="0" x2="567" y2="318" stroke="#fff" stroke-width="6"/>
  </svg>
  <div class="abs" style="left:621px;top:65px;color:#fff;font-size:17px">Need Help?</div>
  <h2 class="abs heading" style="left:621px;top:114px;color:#fff;font-size:31px;line-height:38px">Need Any Help?<br>We Are Available 24/7</h2>
  <div class="btn" style="left:619px;top:208px;width:119px;height:41px;font-size:12px">Contact Us</div>
</section>

<section class="blogs">
  <div class="abs eyebrow centered" style="top:3299px">Blog &amp; News</div>
  <h2 class="abs heading centered" style="top:3338px;font-size:30px">Our Latest Blogs</h2>
  <div class="arrow light" style="left:110px;top:3586px">‹</div>
  <div class="arrow olive" style="left:1058px;top:3586px">›</div>
  <article class="post" style="left:184px">
    <div class="pic" role="img" aria-label="Family meeting with an attorney in a library office" style="background:linear-gradient(135deg,#6c5a4a,#2a2420)"></div>
    <h3>Are there alternatives to divorcing in court?</h3>
    <p>There are many reasons couples choose to resolve financial and children issues that arise.</p>
    <div class="more">Read More ⟶</div>
  </article>
  <article class="post" style="left:469px">
    <div class="pic" role="img" aria-label="Upset couple sitting apart" style="background:linear-gradient(135deg,#b0a89e,#4a423c)"></div>
    <h3>No fault divorce: where are we now?</h3>
    <p>The reasons for a separation are invariably complex and various. The idea of trying to detail.</p>
    <div class="more">Read More ⟶</div>
  </article>
  <article class="post" style="left:755px">
    <div class="pic" role="img" aria-label="Man in distress as a woman leaves through a doorway" style="background:linear-gradient(135deg,#d6cbbd,#6d6052)"></div>
    <h3>Parental alienation and its long term impact</h3>
    <p>Parental Alienation is a difficult, complicated and emotive subject. It involves one parent trying to ensure.</p>
    <div class="more">Read More ⟶</div>
  </article>
</section>

<footer class="footer">
  <h2 class="abs heading" style="left:186px;top:96px;font-size:30px;line-height:40px">Get Update By Signup<br>Newsletter.</h2>
  <div class="abs" style="left:590px;top:81px;width:426px;height:74px;border-radius:37px;background:#fff"></div>
  <svg class="abs" style="left:632px;top:111px" width="18" height="14" viewBox="0 0 18 14"><rect width="18" height="14" rx="2" fill="#555"/><path d="M1 1l8 6 8-6" stroke="#fff" stroke-width="1.5" fill="none"/></svg>
  <div class="abs" style="left:672px;top:111px;color:#999;font-size:11.5px">Enter your email</div>
  <div class="btn" style="left:882px;top:95px;width:117px;height:48px;border-radius:24px;color:#fff;font-family:'Montserrat',sans-serif;font-size:14px">Subscribe</div>

  <div class="logo" style="left:186px;top:246px"><i style="width:28px;height:28px"></i><span style="font-size:12px;line-height:13px">KELLOW<br><span style="font-size:8px">FAMILY LAW</span></span></div>
  <p class="about">Kellow Family Law, collaborative law and unbundled legal services in King County, Washington state</p>
  <div class="abs" style="left:186px;top:374px;font-size:10px;letter-spacing:14px">■■■■</div>

  <h4 style="left:485px">Quick Links</h4>
  <ul style="left:485px"><li>Home</li><li>Our Service</li><li>News</li><li>Videos</li><li>Contact</li></ul>
  <h4 style="left:648px">Help</h4>
  <ul style="left:648px"><li>Who We Are</li><li>Careers</li><li>Advertise With Us</li><li>Privacy Policy</li><li>Terms And Conditions</li></ul>
  <h4 style="left:803px">Contact Us</h4>
  <div class="contact-row" style="top:298px"><svg width="13" height="13" viewBox="0 0 13 13"><path d="M2 1h3l1 3-2 1a7 7 0 0 0 4 4l1-2 3 1v3a1 1 0 0 1-1 1A11 11 0 0 1 1 2a1 1 0 0 1 1-1z" fill="#fff"/></svg><span>(00) 0555 210 478</span></div>
  <div class="contact-row" style="top:335px"><svg width="13" height="10" viewBox="0 0 13 10"><rect width="13" height="10" rx="1" fill="#fff"/><path d="M1 1l5.5 4L12 1" stroke="#0f0f10" fill="none"/></svg><span>office@kellowlaw.com</span></div>
  <div class="contact-row" style="top:372px"><svg width="11" height="14" viewBox="0 0 11 14"><path d="M5.5 0A5.5 5.5 0 0 0 0 5.5C0 9 5.5 14 5.5 14S11 9 11 5.5A5.5 5.5 0 0 0 5.5 0z" fill="#fff"/><circle cx="5.5" cy="5.5" r="2" fill="#0f0f10"/></svg><span>Lorem ipsum dolor sit amet, consectetur adipisicing elit,</span></div>

  <div class="abs" style="left:0;top:498px;width:1200px;text-align:center;font-size:11.5px">Copyright: 2021 Kellow Family Law</div>
</footer>

</body>
</html>
```